Custom Real Estate Flyer

Hi, I'm looking for a classy custom flyer to market residential homes listed for sale in Southern California. I've uploaded my logo's and I'd like to incorporate the logo's into my flyer for branding. I"d like something classy that really showcases pictures of the home for sale. Thank you so much!

8 1/2 x 11 sized page, either one or two sided with maybe logo on back like business card :)
Updates

Thank you everyone! I appreciate your designs very much! :) Please continue to submit.

Target Market(s)

This flyer will showcase my listings and potential clients will see it in my open houses. Hoping for something original and that is memorable :)

Industry/Entity Type

Residential

Requirements
Must have
• **ALL INFO AND LOGO'S ON MY BUSINESS CARD MUST BE ON THE FLYER** (legal requirements), also I want to be able to edit the text and change the pictures on the flyer for all of my listings :)

The word REALTOR must be in all caps and have the "R" in the circle (please refer to business card)

Must have my license number: CalBRE #04738215 (no changes, please refer to business card)

My logo should remain the same.

Please use the Homestead Partners logo submitted.

Nice to have
• I like a fade in the background, and borders around the house pictures.

I'd like a bullet point section and a paragraph section if possible :)

Should not have
• Flyer does not need a mobile scan code.

I don't care for slanted or cut off photo's of the home.

```html
<!DOCTYPE html>
<html lang="en">
<head>
<meta charset="utf-8">
<title>Listing Flyer – 18420 Juniper Ridge Road</title>
<link href="https://fonts.googleapis.com/css2?family=Montserrat:wght@400;500;600&family=Lobster&family=Grand+Hotel&display=swap" rel="stylesheet">
<style>
  :root{
    --navy:#1f4f8a;
    --navy-deep:#173e70;
    --orange:#e8693a;
    --ink:#222;
    --mist:#d5e1ea;
    --mist-light:#eaf0f4;
    --paper:#ffffff;
    --backdrop:#8a8a8a;
  }
  *{box-sizing:border-box;margin:0;padding:0}
  html,body{width:1200px;height:900px;overflow:hidden;background:var(--backdrop)}
  body{font-family:"Montserrat",Arial,sans-serif;color:var(--ink);position:relative}

  .flyer{position:absolute;left:270px;top:23px;width:660px;height:854px;background:var(--paper);overflow:hidden;
    box-shadow:0 6px 24px rgba(0,0,0,.25)}
  .flyer-fade{position:absolute;left:0;top:300px;width:100%;height:360px;
    background:linear-gradient(180deg,var(--mist-light) 0%,var(--mist) 40%,var(--mist) 100%)}

  .brand-block{position:absolute;left:40px;top:0;width:135px;height:120px;background:var(--navy);
    display:flex;align-items:center;justify-content:center;gap:7px;padding:0 8px}
  .brand-block .dot{width:10px;height:10px;background:var(--paper);flex:none}
  .brand-block .name{color:var(--paper);font-weight:600;font-size:12px;line-height:1.25;text-transform:uppercase;letter-spacing:.5px}

  .property-address{position:absolute;left:200px;top:24px;color:var(--orange);font-size:17px;font-weight:500;line-height:1.25;letter-spacing:.3px;text-transform:uppercase}

  .photo{border:4px solid var(--paper);box-shadow:0 1px 3px rgba(0,0,0,.2)}
  .hero-photo{position:absolute;left:66px;top:86px;width:560px;height:290px;
    background:linear-gradient(180deg,#9cc4e6 0%,#d8dde0 45%,#c9c5bd 65%,#5f9a3a 85%,#4f8a2f 100%)}

  .listing-info{position:absolute;left:66px;top:400px;width:252px}
  .price{font-family:"Lobster",cursive;color:var(--orange);font-size:25px;line-height:1}
  .specs{margin-top:12px;text-align:center;font-size:11px;font-weight:500;line-height:1.6}
  .description{margin-top:16px;font-size:8.6px;line-height:1.45;text-align:justify}

  .gallery{position:absolute;left:330px;top:384px;width:296px;display:grid;grid-template-columns:1fr 1fr;gap:8px}
  .gallery .photo{height:96px}
  .g1{background:linear-gradient(160deg,#e9e4d8,#8e6f4e)}
  .g2{background:linear-gradient(160deg,#f0ece2,#7b5a3f)}
  .g3{background:linear-gradient(160deg,#d9d6cc,#8a4e3a)}
  .g4{background:linear-gradient(160deg,#e4e0d8,#6a4b3c)}

  .agent-band{position:absolute;left:0;top:580px;width:660px;height:274px}
  .agent-photo{position:absolute;left:110px;top:690px;width:96px;height:120px;background:linear-gradient(180deg,#dcdcdc,#5a5a5a)}
  .agent-id{position:absolute;left:228px;top:700px}
  .agent-name{font-family:"Grand Hotel",cursive;color:var(--navy);font-size:30px;line-height:1}
  .agent-title{font-size:14px;font-weight:500;letter-spacing:.5px;margin-top:2px;margin-left:10px}
  .agent-title sup{font-size:8px}
  .license{font-size:12px;font-weight:500;margin-top:18px}

  .contact{position:absolute;right:140px;top:688px;text-align:right;font-size:10.5px;font-weight:500;line-height:1.45}

  .agent-mark{position:absolute;right:0;top:620px;width:120px;height:234px;background:linear-gradient(180deg,var(--navy) 0%,var(--navy-deep) 100%);
    display:flex;flex-direction:column;align-items:center;justify-content:center;gap:8px}
  .agent-mark .dot{width:12px;height:12px;background:var(--paper)}
  .agent-mark .name{color:var(--paper);font-size:13px;font-weight:600;text-align:center;line-height:1.2}
</style>
</head>
<body>
  <article class="flyer">
    <div class="flyer-fade"></div>

    <div class="brand-block">
      <span class="dot"></span>
      <span class="name">Homestead Partners</span>
    </div>

    <h1 class="property-address">18420 Juniper Ridge Road<br>Valencia, CA 91355-2210</h1>

    <div class="photo hero-photo" role="img" aria-label="Front exterior photo of the two-story home with lawn and trees"></div>

    <section class="listing-info">
      <p class="price">Offered At $485,000</p>
      <p class="specs">4 Beds | 2 Baths | 1.5 Bath<br>1,957 SqFt, Built in 1986</p>
      <p class="description">Lorem ipsum dolor sit amet, consectetuer adipiscing elit, sed diam nonummy nibh euismod tincidunt ut laoreet dolore magna aliquam erat volutpat. Ut wisi enim ad minim veniam, quis nostrud exerci tation ullamcorper suscipit lobortis nisl ut aliquip ex ea commodo consequat.</p>
    </section>

    <div class="gallery">
      <div class="photo g1" role="img" aria-label="Interior photo of the dining area"></div>
      <div class="photo g2" role="img" aria-label="Interior photo of the living room"></div>
      <div class="photo g3" role="img" aria-label="Interior photo of the family room with fireplace"></div>
      <div class="photo g4" role="img" aria-label="Interior photo of the main bedroom"></div>
    </div>

    <svg class="agent-band" viewBox="0 0 660 274" aria-hidden="true">
      <path d="M0 70 Q330 -30 660 40 L660 274 L0 274 Z" fill="#ffffff"/>
    </svg>

    <div class="agent-photo" role="img" aria-label="Portrait photo of the agent"></div>

    <div class="agent-id">
      <p class="agent-name">Dana Whitfield</p>
      <p class="agent-title">REALTOR<sup>®</sup></p>
      <p class="license">CalBRE #04738215</p>
    </div>

    <address class="contact" style="font-style:normal">
      31750 Cedar Hollow Ave<br>
      Santa Clarita, CA 91350<br>
      661.555.0142 (Cell)<br>
      661.555.0190 VM 2210 (Office)<br>
      www.DanaWhitfield.com<br>
      Dana@DanaWhitfield.com
    </address>

    <div class="agent-mark">
      <span class="dot"></span>
      <span class="name">Dana<br>Whitfield</span>
    </div>
  </article>
</body>
</html>
```